WBP Business Cards

I need business cards for "willow bend partners llc" doublesided... logo on the back (also include logo on front)
logo attached to project... i have jpg up.. let me know if you need eps file.
Company Info:
742 East Harlow Avenue, Suite 8D
Chicago, Illinois 60417
facsimile 312-481-2267 (list fax, address, website on all cards.)
www.willowbendpartnersllc.example
Three different people on cards:
Darius K. Whitcomb, CPA MST
Principal
ofc 312-481-3900
mobile 312-574-8816
dariuskwhitcomb@willowbendpartnersllc.example
Peter J. Olundsen, CPA MST
Principal
peterjolundsen@willowbendpartnersllc.example
mobile 708-613-4471
ofc 312-481-3900
Alvin M Crandby
Principal
ofc 312-481-3900
no mobile
alvinmcrandby@willowbendpartnersllc.example
I have multiple projects listed.. see below:
Business cards for willow bend partners llc
letterhead
envelopes
Business cards for KT Holdings LLC
letterhead
envelopes
Target Market(s)
rich people
Industry/Entity Type
Business
Look and feel

```html
<!DOCTYPE html>
<html lang="en">
<head>
<meta charset="utf-8">
<title>Willow Bend Partners LLC – Business Cards</title>
<link rel="stylesheet" href="https://fonts.googleapis.com/css2?family=Cinzel:wght@400;600&family=Open+Sans:wght@400;600&display=swap">
<style>
  :root {
    --page-bg: #e8e5e0;
    --card-bg: #f4f4f5;
    --navy: #1d4a80;
    --navy-deep: #143766;
    --sky: #4aa6dc;
    --sky-pale: #a9d8f2;
    --ink-blue: #1f4f87;
    --ink: #2b2f38;
    --white: #ffffff;
  }
  * { box-sizing: border-box; margin: 0; padding: 0; }
  html, body {
    width: 1200px; height: 1044px; overflow: hidden;
    background: var(--page-bg);
  }
  .canvas { position: relative; width: 1200px; height: 1044px; }

  .card {
    position: absolute;
    width: 640px; height: 366px;
    background: var(--card-bg);
    box-shadow: 0 6px 18px rgba(0,0,0,0.18);
    overflow: hidden;
  }
  .card--front { left: 80px; top: 110px; }
  .card--back  { left: 480px; top: 570px; }

  .front-panel { position: absolute; inset: 0; width: 640px; height: 366px; }

  .front-url {
    position: absolute; left: 22px; top: 30px;
    font: 400 13px "Open Sans", sans-serif; color: var(--white);
  }
  .front-address {
    position: absolute; left: 22px; top: 200px;
    font: 400 12px/1.45 "Open Sans", sans-serif; color: var(--white);
  }
  .front-phones {
    position: absolute; left: 22px; top: 280px; list-style: none;
    font: 400 12.5px/1.8 "Open Sans", sans-serif; color: var(--white);
  }
  .front-phones li { display: flex; align-items: center; gap: 8px; }
  .front-phones svg { width: 13px; height: 13px; }

  .wordmark {
    font-family: "Cinzel", serif; font-weight: 600;
    color: var(--ink-blue); white-space: nowrap; text-align: center;
  }
  .front-wordmark {
    position: absolute; left: 265px; width: 380px; top: 135px; font-size: 19px;
  }
  .person {
    position: absolute; left: 265px; width: 380px; top: 210px; text-align: center;
    font-family: "Cinzel", serif; color: var(--ink-blue);
  }
  .person-name { font-size: 17px; font-weight: 600; letter-spacing: 0.5px; }
  .person-title { font-size: 13px; margin-top: 2px; letter-spacing: 1px; }
  .person-contact {
    position: absolute; left: 265px; width: 380px; top: 290px; text-align: center;
    font: 400 11px/1.5 "Open Sans", sans-serif; color: var(--ink);
  }

  .back-wordmark {
    position: absolute; left: 0; right: 0; top: 160px; font-size: 27px;
  }
  .back-url {
    position: absolute; left: 0; right: 0; top: 225px; text-align: center;
    font: 600 12px "Open Sans", sans-serif; letter-spacing: 2px; color: var(--ink-blue);
  }
</style>
</head>
<body>
<main class="canvas">

  <section class="card card--front" aria-label="Business card front">
    <svg class="front-panel" viewBox="0 0 640 366" aria-hidden="true">
      <path d="M0 0 H335 C255 60 215 170 235 262 C248 320 280 350 302 366 H0 Z" fill="var(--navy)"/>
      <path d="M335 0 H395 C300 50 250 140 258 230 C263 290 300 340 330 366 H302 C280 350 248 320 235 262 C215 170 255 60 335 0 Z" fill="var(--navy-deep)"/>
      <path d="M232 250 C240 310 270 345 300 366" stroke="var(--sky)" stroke-width="9" fill="none"/>
      <path d="M246 250 C254 305 285 342 318 366" stroke="var(--sky-pale)" stroke-width="4" fill="none"/>
      <path d="M222 262 C232 318 262 350 284 366" stroke="var(--sky-pale)" stroke-width="2" fill="none" opacity="0.7"/>
    </svg>

    <p class="front-url">www.willowbendpartnersllc.example</p>
    <address class="front-address">742 East Harlow Avenue,<br>Suite 8D, Chicago,<br>Illinois 60417</address>
    <ul class="front-phones">
      <li>
        <svg viewBox="0 0 14 14" aria-label="Office"><circle cx="7" cy="7" r="6.5" fill="var(--white)"/><path d="M4.5 4 L6 4 L6.6 5.8 L5.7 6.5 C6.2 7.6 6.9 8.3 8 8.8 L8.7 7.9 L10.5 8.5 L10.5 10 C7 10 4.5 7.5 4.5 4 Z" fill="var(--navy)"/></svg>
        312-481-3900
      </li>
      <li>
        <svg viewBox="0 0 14 14" aria-label="Fax"><circle cx="7" cy="7" r="6.5" fill="var(--white)"/><rect x="4" y="6" width="6" height="4" fill="var(--navy)"/><rect x="5" y="3.5" width="4" height="2.5" fill="var(--navy)"/></svg>
        312-481-2267
      </li>
    </ul>

    <p class="wordmark front-wordmark">Willow Bend Partners llc</p>
    <div class="person">
      <p class="person-name">Darius K. Whitcomb, CPA MST</p>
      <p class="person-title">Principal</p>
    </div>
    <p class="person-contact">
      Email: dariuskwhitcomb@willowbendpartnersllc.example<br>
      Mobile: 312-574-8816
    </p>
  </section>

  <section class="card card--back" aria-label="Business card back">
    <p class="wordmark back-wordmark">Willow Bend Partners llc</p>
    <p class="back-url">www.willowbendpartnersllc.example</p>
  </section>

</main>
</body>
</html>
```